Cobra Vane Systems Website Revamp

We need a full website for the oil and gas sector to showcase our company and our technology/services we provide to larger corporations. We want our website represent innovation and identity.

Background:

We are a service based company that specializes in:

- well services, and
-permanent applications
**(Please be aware that these are two different aspects to the oil and gas sector, both of which we supply to our customers)

We provide a wide range of jet pump technologies to address under performing reservoirs or problematic well producing conditions. We have field operations currently in: Canada, Oman, and Australia with efforts currently underway to expand in other markets. Therefore are needing a website to help promote a better comprehension of what we do and how we can solve their well issues. We are looking for

1.) Identity;
2.) Emphasis on better comprehension of our services for our clients to relate to us as a solution to their needs;
3.) User friendly interface - but new and exciting in this digital age .

Some examples of websites we like:

http://brindlowinc.com/how-we-work/
http://www.qorvantix.com/qorvan-system/
https://velmorafield.com/

Videos of our technologies:

https://www.clipvarro.com/watch?v=519KdpQWzRe
https://www.clipvarro.com/watch?v=t7NBwuhsp43

Target Market(s)

Petroleum Industry Clients

Coding

Coded - Design and coding required

Number of Pages Required

5+ page

Colors

Designer to choose colors to be used in the design.

Requirements
Must have
• See Project Description, and feel free to contact us with any questions/inquiries!
Nice to have
• Our color scheme is generally 'blue', to depict jet pumps (our service). However, we are open to ideas and artistic interpretation. Grayscale/offset colors/highlight colors etc.

```html
<!DOCTYPE html>
<html lang="en">
<head>
<meta charset="utf-8">
<title>Cobra Vane Systems</title>
<link href="https://fonts.googleapis.com/css2?family=Lato:wght@400;700;900&display=swap" rel="stylesheet">
<style>
:root{
  --blue-deep:#0d4f9a;
  --blue-mid:#1a74c4;
  --blue-bright:#27aae6;
  --blue-pale:#bfe3f6;
  --navy:#123f7d;
  --ink:#222;
  --grey-bg:#ececec;
  --footer-bg:#e2e2e2;
  --white:#fff;
}
*{margin:0;padding:0;box-sizing:border-box}
html,body{width:676px;height:1200px;overflow:hidden;background:var(--white)}
body{position:relative;font-family:'Lato',sans-serif;color:var(--ink)}
.abs{position:absolute}

/* header */
.site-header{position:absolute;left:0;top:0;width:676px;height:57px;background:var(--white)}
.brand{position:absolute;display:flex;align-items:center;gap:6px;font-weight:700;color:var(--navy);font-size:15px;white-space:nowrap}
.brand .dot{width:10px;height:10px;border-radius:50%;background:var(--blue-bright)}
.site-header .brand{left:96px;top:20px}
.main-nav{position:absolute;left:295px;top:29px;display:flex;gap:14px;font-size:8.5px;font-weight:700}
.main-nav span::after{content:"";display:inline-block;width:4px;height:4px;border-right:1px solid #666;border-bottom:1px solid #666;transform:rotate(45deg);margin:0 0 2px 5px}
.social{position:absolute;left:510px;top:10px;display:flex;gap:14px}
.social i{width:8px;height:8px;border-radius:50%;background:var(--blue-bright);display:block}
.dropdown{position:absolute;left:506px;top:51px;width:86px;background:var(--blue-bright);z-index:5}
.dropdown::before{content:"";position:absolute;left:14px;top:-5px;border:5px solid transparent;border-top:0;border-bottom-color:var(--blue-bright)}
.dropdown a{display:block;color:var(--white);font-size:8.5px;padding:5px 11px;text-decoration:none}
.dropdown a+a{border-top:1px solid rgba(255,255,255,.35)}

/* hero */
.hero{position:absolute;left:0;top:57px;width:676px;height:284px;background:linear-gradient(180deg,#4a4038 0%,#b7773a 30%,#5b4a3c 48%,#3b3733 75%,#55504a 100%)}
.hero-text{position:absolute;left:0;width:676px;text-align:center;color:var(--white)}
.hero-kicker{top:83px;font-size:18px;letter-spacing:2px;font-weight:400}
.hero-title{top:100px;font-size:32px;font-weight:900}
.hero-lede{top:142px;font-size:12px;line-height:15px}
.arrow{position:absolute;width:18px;height:18px;border-left:1.5px solid var(--white);border-bottom:1.5px solid var(--white)}
.arrow.left{transform:rotate(45deg)}
.arrow.right{transform:rotate(-135deg)}
.arrow.dark{border-color:#555}
.dots{position:absolute;left:317px;top:253px;display:flex;gap:5px}
.dots i{width:7px;height:7px;border-radius:50%;background:var(--white);display:block}
.dots i:first-child{background:transparent;border:1px solid var(--white)}

/* challenge */
.challenge-bg{position:absolute;left:0;top:341px}
.section-title{position:absolute;left:0;width:676px;text-align:center;font-weight:900;font-size:15px}
.challenge-title{top:376px;color:var(--white)}
.challenge-copy{position:absolute;left:128px;top:406px;width:420px;text-align:center;color:var(--white);font-size:8px;line-height:14.6px}
.btn{position:absolute;display:flex;align-items:center;justify-content:center;color:var(--white);font-weight:900;font-size:9px}
.btn.navy{left:286px;top:478px;width:104px;height:25px;background:var(--navy)}
.feature{position:absolute;width:110px;text-align:center}
.feature svg{display:block;margin:0 auto}
.feature p{color:var(--blue-mid);font-weight:700;font-size:9px;line-height:11px;margin-top:10px}

/* solution */
.solution{position:absolute;left:0;top:659px;width:676px;height:291px;background:linear-gradient(90deg,#f7f7f7,#e3e3e3)}
.solution-title{top:682px;color:#222}
.solution-heading{position:absolute;left:99px;top:739px;color:var(--blue-mid);font-weight:700;font-size:14px}
.solution-copy{position:absolute;left:100px;top:767px;width:235px;font-size:8px;line-height:12px;color:#333}
.btn.sky{left:102px;top:881px;width:91px;height:23px;background:var(--blue-mid)}
.photo-ring{position:absolute;left:349px;top:720px;width:198px;height:198px;border-radius:50%;background:#f4f4f4;box-shadow:0 2px 8px rgba(0,0,0,.15)}
.photo{position:absolute;left:361px;top:732px;width:174px;height:174px;border-radius:50%;background:linear-gradient(180deg,#8a8f96 0%,#a9adb2 45%,#6d6a64 75%,#d9d9d9 100%)}

/* info boxes */
.area{position:absolute;left:106px;top:976px;width:230px;height:110px;border:1px solid #999;background:var(--white)}
.area h3{text-align:center;font-size:11px;font-weight:900;margin-top:17px}
.area ul{list-style:none;position:absolute;left:14px;top:44px;display:grid;grid-template-columns:72px 66px 80px;row-gap:6px;font-size:7.5px}
.area li{display:flex;align-items:center;gap:4px}
.area li i{width:7px;height:7px;border-radius:50%;background:var(--blue-mid);display:block}
.contact-box{position:absolute;left:345px;top:977px;width:229px;height:109px;background:linear-gradient(135deg,var(--blue-deep),var(--blue-bright));color:var(--white)}
.contact-box h3{text-align:center;font-size:11px;font-weight:900;margin-top:17px}
.phones{position:absolute;left:23px;top:49px;display:flex;gap:12px;font-size:11.5px;font-weight:700;align-items:center}
.phones span{display:flex;align-items:center;gap:3px}

/* footer */
.site-footer{position:absolute;left:0;top:1130px;width:676px;height:70px;background:var(--footer-bg)}
.footer-nav{position:absolute;left:108px;top:19px;display:flex;gap:18px;font-size:7.5px;font-weight:700}
.copyright{position:absolute;left:108px;top:34px;font-size:7px;color:#444}
.site-footer .brand{left:426px;top:20px;font-size:13px}
</style>
</head>
<body>

<header class="site-header">
  <div class="brand"><span class="dot"></span>Cobra Vane Systems</div>
  <div class="social"><i></i><i></i><i></i></div>
  <nav class="main-nav">
    <span>What we do</span><span>Who we are</span><span>Products &amp; Service</span><span>Contact Us</span>
  </nav>
  <div class="dropdown"><a>Location</a><a>Enquiry</a></div>
</header>

<section class="hero" role="img" aria-label="Jet pump skid with red electric motor on a wellsite at sunset"></section>
<div class="hero-text hero-kicker">WELCOME TO</div>
<div class="hero-text hero-title">COBRA VANE SYSTEMS</div>
<div class="hero-text hero-lede">Lorem ipsum dolor sit amet consectetuer adipiscing elit Nam<br>cursus Morbi ut mi Nullam enim leo egestas</div>
<span class="arrow left" style="left:92px;top:176px"></span>
<span class="arrow right" style="left:566px;top:176px"></span>
<div class="dots"><i></i><i></i><i></i><i></i></div>

<svg class="challenge-bg" width="676" height="230" viewBox="0 0 676 230">
  <defs>
    <linearGradient id="challengeGrad" x1="0" y1="1" x2="1" y2="0">
      <stop offset="0" stop-color="#0d4f9a"/><stop offset="1" stop-color="#27aae6"/>
    </linearGradient>
  </defs>
  <path d="M0 160 Q338 240 676 172 L676 186 Q338 250 0 168 Z" fill="#bfe3f6"/>
  <path d="M0 0 H676 V172 Q338 235 0 160 Z" fill="url(#challengeGrad)"/>
</svg>
<h2 class="section-title challenge-title">THE CHALLENGE</h2>
<p class="challenge-copy">When it comes to resolving an effective artificial lift strategy over a horizontal well's life cycle, there are many complications and compromises. Torvel Systems™ has developed an artificial lift solution that addresses some of the most common challenges in horizontal wells – solids, gas interference, slug flow. The Torvel System™ gives you the freedom to optimize your artificial lift strategy over the life of the well.</p>
<div class="btn navy">LEARN MORE</div>

<div class="feature" style="left:130px;top:526px">
  <svg width="62" height="62" viewBox="0 0 62 62"><circle cx="31" cy="31" r="29" fill="#fff" stroke="#0d4f9a" stroke-width="3.5"/><g fill="none" stroke="#1a74c4" stroke-width="1.5"><rect x="19" y="18" width="24" height="5"/><path d="M24 23v16h14V23M27 39v6M35 39v6M24 30h14"/></g></svg>
  <p>PERMANENT<br>ARTIFICIAL LIFT</p>
</div>
<div class="feature" style="left:232px;top:526px">
  <svg width="62" height="62" viewBox="0 0 62 62"><circle cx="31" cy="31" r="29" fill="#fff" stroke="#0d4f9a" stroke-width="3.5"/><g fill="none" stroke="#1a74c4" stroke-width="1.5"><path d="M34 14v18M31 20h6M31 26h6M18 32h28v6H18zM22 38v8M42 38v8M16 46h32"/><rect x="22" y="27" width="8" height="5"/></g></svg>
  <p>WELL<br>SERVICES</p>
</div>
<div class="feature" style="left:335px;top:526px">
  <svg width="62" height="62" viewBox="0 0 62 62"><circle cx="31" cy="31" r="29" fill="#fff" stroke="#0d4f9a" stroke-width="3.5"/><g fill="none" stroke="#1a74c4" stroke-width="1.5"><path d="M24 44s-6-7-6-11a6 6 0 0 1 12 0c0 4-6 11-6 11z"/><circle cx="24" cy="33" r="2"/><path d="M39 28s-5-6-5-9a5 5 0 0 1 10 0c0 3-5 9-5 9z"/><path d="M29 44h10a3 3 0 0 0 0-6h-5" stroke-dasharray="2 2"/></g></svg>
  <p>LOCATIONS</p>
</div>
<div class="feature" style="left:438px;top:526px">
  <svg width="62" height="62" viewBox="0 0 62 62"><circle cx="31" cy="31" r="29" fill="#fff" stroke="#0d4f9a" stroke-width="3.5"/><g fill="none" stroke="#1a74c4" stroke-width="1.5"><rect x="30" y="18" width="16" height="11"/><path d="M30 18l8 6 8-6"/><path d="M19 30c0 8 6 14 14 14l3-4-4-3-2 2c-3-1-5-3-6-6l2-2-3-4z"/></g></svg>
  <p>CONTACT US</p>
</div>

<section class="solution"></section>
<h2 class="section-title solution-title">THE SOLUTION</h2>
<span class="arrow left dark" style="left:68px;top:787px"></span>
<span class="arrow right dark" style="left:570px;top:787px"></span>
<h3 class="solution-heading">Horizontal &amp; Deviated Wells</h3>
<p class="solution-copy">ith no moving parts, the SVX jet pump takes the industry to the next level, allowing for jet pump placement anywhere in the horizontal profile. Using power fluid as the drive mechanism of a jet pump, the system has no problems with deviated, crooked or horizontal wellbores.<br>With a jet pump landed in the horizontal section of a well, operators are not only able to achieve higher inflow rates, they are also able to achieve higher ultimate reserve recovery</p>
<div class="btn sky">LEARN MORE</div>
<div class="photo-ring"></div>
<div class="photo" role="img" aria-label="Wellhead with valves and piping beside a white building on snowy ground"></div>

<div class="area">
  <h3>AREA OF OPERATION</h3>
  <ul>
    <li><i></i>Sales</li><li><i></i>Service</li><li><i></i>Administration</li>
    <li><i></i>Engineering</li><li><i></i>Accounting</li><li><i></i>Well Analysis</li>
    <li><i></i>Operations</li>
  </ul>
</div>
<div class="contact-box">
  <h3>CONTACT US</h3>
  <div class="phones">
    <span><svg width="10" height="10" viewBox="0 0 10 10"><rect x="1" y="2" width="8" height="7" fill="none" stroke="#fff" stroke-width="1.2"/><rect x="3" y="0.5" width="4" height="2" fill="#fff"/></svg>555.014.2270</span>
    <span><svg width="11" height="11" viewBox="0 0 11 11"><path d="M1 2c0 5 3 8 8 8l1.5-2-2-1.5-1 1C5.5 7 4 5.5 3.5 3.5l1-1L3 0.5z" fill="none" stroke="#fff" stroke-width="1.2"/></svg>1.800.555.0199</span>
  </div>
</div>

<footer class="site-footer">
  <nav class="footer-nav"><span>What we do</span><span>Who we are</span><span>Products &amp; Service</span><span>Contact Us</span></nav>
  <p class="copyright">© 2018 Company Name  All right reserved</p>
  <div class="brand"><span class="dot"></span>Cobra Vane Systems</div>
</footer>

</body>
</html>
```